Book Postcard Design

We need a postcard design to promote the book written by our founder and president, Lior Beckett. The book is titled KESTRL: The Craft and Logic of Momentum. We're open to any eye-catching image designs you come up with.

```html
<!DOCTYPE html>
<html lang="en">
<head>
<meta charset="utf-8">
<title>KESTRL Book Postcard</title>
<link href="https://fonts.googleapis.com/css2?family=Montserrat:wght@400;700;800&family=Pathway+Gothic+One&family=Lato:wght@400;700&display=swap" rel="stylesheet">
<style>
  :root{
    --page:#e6e6e4;
    --ink:#1d1d1d;
    --band:#3a3839;
    --band-deep:#2a2829;
    --panel:#eeeeee;
    --white:#ffffff;
    --red:#c8102e;
    --muted:#8a8a8a;
    --rule:#b5b5b5;
    --teal:#5fbfb6;
    --cover-top:#1c1c20;
  }
  *{box-sizing:border-box;margin:0;padding:0}
  html,body{width:932px;height:1200px;overflow:hidden;background:var(--page)}
  body{position:relative;font-family:'Lato',sans-serif;color:var(--ink)}
  .card{position:absolute;left:112px;width:709px;height:472px;background:var(--white);box-shadow:0 4px 14px rgba(0,0,0,.25);overflow:hidden}
  .card--front{top:79px}
  .card--back{top:659px}

  .brand{position:absolute;display:flex;align-items:center;gap:10px}
  .brand__dot{width:50px;height:50px;border-radius:50%;background:var(--red);flex:none}
  .brand__name{font-family:'Montserrat',sans-serif;font-weight:400;font-size:27px;letter-spacing:-.3px;color:var(--ink);white-space:nowrap}
  .card--front .brand{left:22px;top:18px}
  .card--back .brand{left:24px;top:20px}
  .card--back .brand__dot{width:46px;height:46px}
  .card--back .brand__name{font-size:23px}

  .promo{position:absolute;left:0;top:93px;width:709px;height:304px;background:linear-gradient(90deg,var(--band) 0%,var(--band-deep) 100%);color:var(--white);padding:20px 0 0 27px}
  .promo__title{font-family:'Montserrat',sans-serif;font-weight:800;font-size:48px;line-height:1;letter-spacing:.5px}
  .promo__subtitle{font-family:'Pathway Gothic One',sans-serif;font-size:28px;line-height:1;margin-top:8px}
  .promo__body{font-family:'Pathway Gothic One',sans-serif;font-size:12.6px;line-height:15.5px;width:370px;margin-top:14px;color:#ececec}
  .promo__body p+p{margin-top:12px}
  .pillars{list-style:none;margin-top:12px;font-family:'Pathway Gothic One',sans-serif;font-size:12.6px;line-height:16.3px;color:#ececec}
  .pillars b{font-weight:400;font-size:14px;color:var(--white)}

  .book{position:absolute;left:447px;top:28px;width:212px;height:382px;box-shadow:6px 8px 14px rgba(0,0,0,.45)}
  .book__pages{position:absolute;right:-8px;top:8px;width:8px;height:370px;background:linear-gradient(90deg,#ddd,#fff)}
  .book__cover{position:absolute;inset:0;background:linear-gradient(180deg,var(--cover-top) 0%,#22292b 45%,var(--teal) 100%);display:flex;flex-direction:column;align-items:center}
  .book__ring{position:absolute;left:16px;top:26px;width:180px;height:180px;border:2px solid #d9a23a;border-radius:50%;opacity:.8}
  .book__title{font-family:'Montserrat',sans-serif;font-weight:700;font-size:40px;margin-top:98px;color:#d8c070;letter-spacing:1px}
  .book__sub{font-family:'Montserrat',sans-serif;font-weight:700;font-size:10px;color:var(--teal);text-align:center;margin-top:6px;line-height:1.5}
  .book__sub span{font-size:15px}
  .book__author{margin-top:100px;border:2px solid #d9a23a;padding:6px 12px;font-family:'Montserrat',sans-serif;font-weight:700;font-size:11px;letter-spacing:2px;color:var(--ink)}

  .address{position:absolute;left:27px;top:416px;font-size:13.5px;line-height:17px}
  .contact{position:absolute;right:34px;top:416px;text-align:right}
  .contact__phone{font-family:'Lato',sans-serif;font-weight:700;font-size:23px;display:flex;align-items:center;gap:6px;justify-content:flex-end}
  .contact__web{font-style:italic;font-size:12px;color:var(--red)}

  .letter{position:absolute;left:0;top:0;width:359px;height:472px;background:var(--panel)}
  .letter__body{position:absolute;left:22px;top:92px;width:320px;font-size:8.6px;line-height:12.6px;text-align:justify}
  .letter__body p+p{margin-top:5px}
  .signoff{position:absolute;left:0;top:380px;width:359px;height:92px;background:var(--band);color:var(--white)}
  .signoff__photo{position:absolute;left:20px;top:-35px;width:93px;height:112px;border:2px solid var(--white);background:linear-gradient(160deg,#7c8a9a,#3d4f66)}
  .signoff__name{position:absolute;left:127px;top:26px;font-size:13px;font-weight:700;letter-spacing:.2px}
  .signoff__email{position:absolute;left:127px;top:46px;font-size:10.5px}

  .return{position:absolute;left:406px;top:32px;font-family:'Pathway Gothic One',sans-serif;font-size:9.5px;line-height:13px;color:#555}
  .stamp{position:absolute;left:609px;top:31px;width:73px;height:70px;border:1px solid var(--rule)}
  .addr-line{position:absolute;left:457px;width:225px;border-top:1px solid var(--rule)}
  .motto{position:absolute;left:380px;top:408px;width:310px;text-align:center;font-style:italic;font-size:12.5px;line-height:19px;color:var(--red)}
</style>
</head>
<body>

<section class="card card--front">
  <div class="brand"><span class="brand__dot"></span><span class="brand__name">THE HALVERN GROUP</span></div>

  <div class="promo">
    <h1 class="promo__title">KESTRL</h1>
    <h2 class="promo__subtitle">The Craft and Logic of Momentum</h2>
    <div class="promo__body">
      <p>Today, the ability to build momentum is one of the most marketable skills a manager can possess, and the ability to sustain it is vital for anyone who wants to accomplish their vision through others. It is especially required for anyone who has a worthwhile cause.</p>
      <p>Lior Beckett has developed an effective road map that builds momentum. He calls it KESTRL, an acronym for six pillars of lasting change. Here are four of them in greater detail:</p>
    </div>
    <ul class="pillars">
      <li><b>Knowledge:</b> Understanding what drives people to act</li>
      <li><b>Energy:</b> Real focus applied without wasted effort</li>
      <li><b>Strategy:</b> The plan of actions by people toward a shared goal</li>
      <li><b>Timing:</b> Acting when capability, capacity and readiness align.</li>
    </ul>
  </div>

  <div class="book">
    <div class="book__pages"></div>
    <div class="book__cover" role="img" aria-label="Book cover artwork: dark-to-teal gradient with ring illustration behind the title">
      <div class="book__ring"></div>
      <div class="book__title">KESTRL</div>
      <div class="book__sub">THE CRAFT AND LOGIC OF<br><span>MOMENTUM</span></div>
      <div class="book__author">LIOR BECKETT</div>
    </div>
  </div>

  <address class="address" style="font-style:normal">48 Alder Crest Lane<br>Millbrook, NC 28790</address>
  <div class="contact">
    <div class="contact__phone">
      <svg width="22" height="22" viewBox="0 0 24 24" aria-hidden="true"><circle cx="12" cy="12" r="10.5" fill="none" stroke="#1d1d1d" stroke-width="2"/><path d="M8.6 6.8l1.6-.3 1.2 2.6-1 .9c.5 1.3 1.4 2.3 2.6 2.9l.9-1 2.6 1.2-.3 1.6c-.2.6-.8 1-1.5.9-3.3-.6-5.8-3.1-6.4-6.4-.1-.7.3-1.3.9-1.5z" fill="#1d1d1d"/></svg>
      800-555-0147
    </div>
    <div class="contact__web">www.halverngroup.net</div>
  </div>
</section>

<section class="card card--back">
  <div class="letter">
    <div class="brand"><span class="brand__dot"></span><span class="brand__name">THE HALVERN GROUP</span></div>
    <div class="letter__body">
      <p>We know how difficult training can be in your industry. Unlike children, whose sponge-like minds are ripe for training, you work with adults. Adults have unique opinions and established habits that can make them unruly trainees.</p>
      <p>That’s why we’re here. The Halvern Group is a consulting and training organization, and we’ve worked with hundreds of businesses across a dozen industries (including business to business and business to consumer enterprises) to help refine their training and make their business more effective. Businesses experience an average growth of 20% within the first year of working with The Halvern Group.</p>
      <p>We’re the experts on adult behavior change; we know the ins-and-outs of the hows and whys, and we can help you gain that knowledge, too.</p>
      <p>Need proof? That’s why we’ve sent along this copy of KESTRL: The Craft and Logic of Momentum. In this book I break down the six step process I’ve refined to enact adult behavioral change. It’s a quick and easy read, and I think you’ll enjoy it.</p>
      <p>Once you’ve read KESTRL, you might be inspired to change your business. When that happens, give us a call. We’d love to help.</p>
    </div>
    <div class="signoff">
      <div class="signoff__photo" role="img" aria-label="Portrait photo of Lior Beckett speaking at an event"></div>
      <div class="signoff__name">Lior Beckett, Founder &amp; CEO</div>
      <div class="signoff__email">lbeckett@halverngroup.net</div>
    </div>
  </div>

  <div class="return">The Halvern Group<br>48 Alder Crest Lane<br>Millbrook, NC 28790</div>
  <div class="stamp"></div>
  <div class="addr-line" style="top:199px"></div>
  <div class="addr-line" style="top:231px"></div>
  <div class="addr-line" style="top:263px"></div>
  <div class="addr-line" style="top:295px"></div>
  <p class="motto">“The Halvern Group is driven to inspire leaders,<br>influence change and impact profits.”</p>
</section>

</body>
</html>
```